Business Card Design for Engineering Firm

Need a business card design for small mechanical and plumbing engineering form based in Utah. Design should be customizable for all employees.

```html
<!DOCTYPE html>
<html lang="en">
<head>
<meta charset="utf-8">
<title>Halverson Engineering – Business Card</title>
<link href="https://fonts.googleapis.com/css2?family=Montserrat:wght@400;500;700&display=swap" rel="stylesheet">
<style>
  :root {
    --bg-top: #d2d2d2;
    --bg-bottom: #9d9d9d;
    --card-light: #ffffff;
    --card-dark: #2b2b2b;
    --brand-red: #801714;
    --ink: #3a3a3a;
    --grey-mark: #4a4a4a;
    --on-dark: #ffffff;
  }
  * { box-sizing: border-box; margin: 0; padding: 0; }
  html, body { width: 1200px; height: 802px; overflow: hidden; }
  body {
    background: linear-gradient(180deg, var(--bg-top), var(--bg-bottom));
    font-family: "Montserrat", Arial, sans-serif;
    position: relative;
  }
  .card {
    position: absolute;
    top: 246px;
    width: 540px;
    height: 310px;
    border-radius: 22px;
    box-shadow: 0 14px 30px rgba(0,0,0,0.28);
    overflow: hidden;
  }
  /* Front */
  .card--front { left: 40px; background: var(--card-light); }
  .front__info { position: absolute; left: 46px; top: 40px; width: 270px; }
  .brand { color: var(--brand-red); font-weight: 700; font-size: 27px; letter-spacing: 0.5px; line-height: 1; }
  .brand__sub { color: var(--brand-red); font-weight: 700; font-size: 10.5px; letter-spacing: 7px; margin-top: 5px; padding-left: 30px; }
  .person { margin-top: 26px; }
  .person__name { color: var(--brand-red); font-weight: 700; font-size: 16px; letter-spacing: 0.4px; }
  .person__title { color: var(--ink); font-size: 11.5px; margin-top: 3px; }
  .address { color: var(--ink); font-size: 11.5px; line-height: 1.35; margin-top: 12px; }
  .contacts { list-style: none; margin-top: 10px; }
  .contacts li { display: flex; align-items: center; gap: 8px; color: var(--ink); font-size: 11.5px; line-height: 1.5; }
  .contacts svg { width: 10px; height: 10px; flex: none; }
  .front__accent { position: absolute; left: 0; top: 188px; width: 36px; height: 24px; background: var(--brand-red); }
  .front__mark { position: absolute; right: 40px; top: 50px; width: 180px; display: flex; flex-direction: column; align-items: center; gap: 16px; }
  .front__square { width: 150px; height: 150px; background: var(--brand-red); }
  .front__mark-name { color: var(--grey-mark); font-weight: 700; font-size: 14px; letter-spacing: 0.6px; text-align: center; }
  /* Back */
  .card--back { left: 620px; background: var(--card-dark); display: flex; align-items: center; justify-content: center; gap: 22px; }
  .back__square { width: 74px; height: 74px; background: var(--on-dark); }
  .back__divider { width: 2px; height: 110px; background: var(--on-dark); }
  .back__wordmark { color: var(--on-dark); }
  .back__wordmark .name { font-weight: 500; font-size: 34px; letter-spacing: 1px; line-height: 1; }
  .back__wordmark .sub { font-weight: 500; font-size: 14px; letter-spacing: 9px; margin-top: 8px; padding-left: 40px; }
</style>
</head>
<body>
  <section class="card card--front">
    <div class="front__info">
      <div class="brand">HALVERSON</div>
      <div class="brand__sub">ENGINEERING</div>
      <div class="person">
        <div class="person__name">DANIEL REYES</div>
        <div class="person__title">CEO/Founder</div>
      </div>
      <div class="address">4170 Canyon Road<br>Provo, UT 84601</div>
      <ul class="contacts">
        <li><svg viewBox="0 0 10 10"><circle cx="5" cy="5" r="5" fill="var(--brand-red)"/><path d="M3 2.5 L4.3 2.5 L4.8 4 L4 4.6 Q4.7 6 6 6.3 L6.5 5.5 L8 6 L8 7.3 Q5 7.8 2.8 5 Q2.2 3.6 3 2.5Z" fill="#fff"/></svg>801-555-0143</li>
        <li><svg viewBox="0 0 10 10"><circle cx="5" cy="5" r="5" fill="var(--brand-red)"/><rect x="3.5" y="2" width="3" height="6" rx="0.6" fill="#fff"/></svg>801-555-0178</li>
        <li><svg viewBox="0 0 10 10"><circle cx="5" cy="5" r="5" fill="var(--brand-red)"/><rect x="2.3" y="3.2" width="5.4" height="3.8" fill="#fff"/><path d="M2.3 3.2 L5 5.3 L7.7 3.2" stroke="var(--brand-red)" stroke-width="0.6" fill="none"/></svg>info@halversoneng.com</li>
        <li><svg viewBox="0 0 10 10"><circle cx="5" cy="5" r="5" fill="var(--brand-red)"/><circle cx="5" cy="5" r="2.8" fill="none" stroke="#fff" stroke-width="0.7"/><path d="M2.2 5 H7.8 M5 2.2 V7.8" stroke="#fff" stroke-width="0.6"/></svg>www.halversoneng.com</li>
      </ul>
    </div>
    <div class="front__accent"></div>
    <div class="front__mark">
      <div class="front__square"></div>
      <div class="front__mark-name">HALVERSON ENGINEERING</div>
    </div>
  </section>

  <section class="card card--back">
    <div class="back__square"></div>
    <div class="back__divider"></div>
    <div class="back__wordmark">
      <div class="name">HALVERSON</div>
      <div class="sub">ENGINEERING</div>
    </div>
  </section>
</body>
</html>
```